Calderon Lending. Website design for a mortgage company.

We need a simple, but classy and artistic website design. The website should contain a home page, about page, and information page. I would like the design for each page created and I can add the content.

Calderon Lending is a retail mortgage broker business specially crafted to provide simple, transparent, and comprehensive mortgage solutions. We understand the complexities of mortgage acquisition and have aligned with the best partners and resources to analyze the information and deliver precise, transparent, efficient, and reliable results.

Target Market(s)

We are targeting people ages 30-65 within the United States, both male and female. We are also targeting business owners and property investors specifically.

Industry/Entity Type

Mortgage Brokerage

Coding

Coded - Design and coding required

Number of Pages Required

5+ page

Font styles to use
Sans Serif
Script

Requirements
Must have
• The main purpose of this website is to provide clients with the necessary information to want to move forward with a loan transaction. The website will be informational to promote the company and showcase our purpose. The company purpose is to provide efficient and comprehensive service to clients, and to help them navigate the challenging mortgage world.

The website must mimic that of the major fortune 500 companies. It needs to be super clean, but very modern. The pictures should be of families with brown skin mostly.

The website needs to be mobile responsive. Each page needs to consist of large and responsive Hero Images. There will be background videos on the product and process pages of the website.

The website must have a semi-flat design.
The website must have a Hamburger Menu instead of a visible navigation menu.

Use the script font styles for the headlines and the sans serif for body text.

We need to have the following pages:
Home

Products

Process

About

Contact - I want a map of our office location and region. We are located in Bowie MD and our region consists of the following states: Florida, Texas, Virginia, Maryland, and Washington DC.

```html
<!DOCTYPE html>
<html lang="en">
<head>
<meta charset="utf-8">
<title>Calderon Lending — A Retail Mortgage Broker</title>
<link rel="stylesheet" href="https://fonts.googleapis.com/css2?family=Poppins:wght@500;600;700&family=Open+Sans:wght@400;600&display=swap">
<style>
:root{
  --navy:#0c426e;
  --navy-deep:#093760;
  --navy-soft:#124e7f;
  --ink:#1b1b1b;
  --text:#333;
  --grey-panel:#6e6e6e;
  --rule:#d8d8d8;
  --quote-bg:#e6e6ea;
  --footer:#2b2b2b;
  --white:#fff;
}
*{box-sizing:border-box;margin:0;padding:0}
html,body{width:1200px;height:3541px;overflow:hidden;background:var(--white)}
body{font-family:"Open Sans",Arial,sans-serif;color:var(--text);position:relative}
.abs{position:absolute}
.heading{font-family:"Poppins",Arial,sans-serif;font-weight:700;color:var(--ink)}
.btn{position:absolute;display:flex;align-items:center;justify-content:center;font-family:"Poppins",Arial,sans-serif;font-weight:700;color:var(--white);background:var(--navy);font-size:13px}

/* hero */
.hero{position:absolute;left:0;top:0;width:1200px;height:665px;background:linear-gradient(180deg,#b6c1c8 0%,#8c7a6d 30%,#6d4a3a 45%,#4f6b3a 62%,#3f6a2c 100%)}
.brand{position:absolute;left:133px;top:16px;width:162px;text-align:center}
.brand .mark{width:36px;height:36px;border:3px solid var(--navy);margin:0 auto 8px}
.brand .name{font-family:"Poppins",Arial,sans-serif;font-weight:600;font-size:17px;color:var(--navy);line-height:1}
.brand .tag{font-size:11px;color:#333;letter-spacing:1px;margin-top:3px}
.menu-toggle{position:absolute;left:1033px;top:34px;width:34px;text-align:center;color:var(--navy);font-family:"Poppins",Arial,sans-serif;font-weight:600;font-size:10px}
.menu-toggle span{display:block;height:4px;background:var(--navy);margin-bottom:5px}
.hero h1{position:absolute;left:133px;top:488px;font-size:31px;line-height:36px;color:var(--white)}
.hero .btn{left:136px;top:577px;width:106px;height:32px;background:var(--navy);border:2px solid var(--white);font-size:12px}
.dots{position:absolute;left:562px;top:613px;display:flex;gap:12px;align-items:center}
.dots i{width:6px;height:6px;border-radius:50%;background:var(--white)}
.dots i.on{width:11px;height:11px;border:2px solid var(--white);background:var(--navy)}

/* section titles */
.sec-title{position:absolute;left:0;width:1200px;text-align:center;font-size:26px}
.rule{position:absolute;height:3px;background:var(--navy)}

/* services */
.service{position:absolute;width:356px;text-align:center}
.service svg{display:block;margin:0 auto 20px}
.service h3{font-family:"Poppins",Arial,sans-serif;font-weight:600;font-size:16px;color:var(--ink);margin-bottom:10px}
.service p{font-size:13px;line-height:17.5px}
.vline{position:absolute;width:1px;background:var(--rule);top:793px;height:435px}

/* about */
.about-photo{position:absolute;left:0;top:1303px;width:755px;height:437px;background:linear-gradient(120deg,#d9dcd8 0%,#8f9a93 40%,#6c8a80 60%,#5b5450 100%)}
.about-panel{position:absolute;left:755px;top:1303px;width:445px;height:437px;background:var(--grey-panel);color:var(--white)}
.about-panel .kicker{position:absolute;left:48px;top:48px;font-family:"Poppins",Arial,sans-serif;font-weight:600;font-size:19px}
.about-panel h2{position:absolute;left:48px;top:74px;font-family:"Poppins",Arial,sans-serif;font-weight:600;font-size:26px}
.about-panel .bar{position:absolute;left:48px;top:117px;width:34px;height:3px;background:var(--white)}
.about-panel p{position:absolute;left:48px;top:151px;width:270px;font-size:13.5px;line-height:17.6px}
.about-panel .btn{left:50px;top:355px;width:102px;height:34px;font-size:11px}

/* why */
.why{position:absolute;left:0;top:1740px;width:1200px;height:593px;background:var(--navy)}
.why h2{position:absolute;left:133px;top:57px;font-size:25px;color:var(--white)}
.why .bar{position:absolute;left:133px;top:96px;width:56px;height:3px;background:var(--white)}
.reason{position:absolute;left:133px;width:406px;height:98px}
.reason.active{background:var(--navy-soft)}
.reason .ico{position:absolute;left:24px;top:24px;width:54px;height:54px;border-radius:50%;border:1px solid #5d86ab;display:flex;align-items:center;justify-content:center}
.reason.active .ico{background:var(--white);border-color:var(--white)}
.reason h4{position:absolute;left:98px;top:16px;font-family:"Poppins",Arial,sans-serif;font-weight:600;font-size:16px;color:var(--white)}
.reason p{position:absolute;left:98px;top:45px;width:260px;font-size:12px;line-height:16.5px;color:#e4ecf3}
.why-photo{position:absolute;left:540px;top:63px;width:524px;height:473px;background:linear-gradient(180deg,#2a6bd6 0%,#2d4f8d 40%,#6a5a35 65%,#3e6fb8 100%)}

/* testimonials */
.t-card{position:absolute;top:2478px;width:224px;height:285px;border:1px solid #cfcfcf;background:var(--white)}
.t-card .q{position:absolute;left:16px;top:14px;font-family:"Poppins",Arial,sans-serif;font-weight:700;font-size:26px;color:var(--navy);line-height:1}
.t-card .stars{position:absolute;left:34px;top:45px;color:var(--navy);font-size:10px;letter-spacing:1px}
.t-card p{position:absolute;left:34px;top:63px;width:170px;font-size:12px;line-height:16px}
.t-card .bar{position:absolute;left:34px;top:236px;width:28px;height:3px;background:var(--navy)}
.t-card .who{position:absolute;left:34px;top:248px;font-family:"Poppins",Arial,sans-serif;font-weight:600;font-size:11px;color:var(--navy)}
.arrow{position:absolute;top:2598px}

/* quote band */
.quote{position:absolute;left:0;top:2826px;width:1200px;height:303px;background:var(--quote-bg);text-align:center}
.quote h2{position:absolute;left:0;top:66px;width:1200px;font-size:26px}
.quote p{position:absolute;left:290px;top:122px;width:620px;font-size:15px;line-height:23px}
.quote .btn{left:432px;top:189px;width:336px;height:48px;font-size:14px}

/* footer */
.footer{position:absolute;left:0;top:3129px;width:1200px;height:412px;background:var(--footer);color:#e8e8e8}
.f-brand{position:absolute;left:173px;top:97px;width:162px;text-align:center}
.f-brand .mark{width:40px;height:40px;border:3px solid var(--white);margin:0 auto 10px}
.f-brand .name{font-family:"Poppins",Arial,sans-serif;font-weight:600;font-size:17px;color:var(--white);line-height:1}
.f-brand .tag{font-size:11px;letter-spacing:1px;margin-top:3px}
.f-col h5{position:absolute;font-family:"Poppins",Arial,sans-serif;font-weight:600;font-size:15px;color:var(--white);letter-spacing:.5px}
.f-menu{position:absolute;left:458px;top:104px;list-style:none;font-size:14px;line-height:24.2px}
.f-item{position:absolute;display:flex;align-items:flex-start;gap:14px;font-size:14px;line-height:19px}
.f-item .dot{flex:none;width:28px;height:28px;border-radius:50%;background:var(--white);display:flex;align-items:center;justify-content:center}
.f-rule{position:absolute;left:128px;top:323px;width:939px;height:1px;background:#4a4a4a}
.copy{position:absolute;left:0;top:360px;width:1200px;text-align:center;font-size:11px}
</style>
</head>
<body>

<header class="hero" role="img" aria-label="Large red-brick family home with a green lawn under a soft sky">
  <div class="brand">
    <div class="mark"></div>
    <div class="name">CALDERON LENDING</div>
    <div class="tag">a retail mortgage broker</div>
  </div>
  <div class="menu-toggle"><span></span><span></span><span></span>MENU</div>
  <h1 class="heading">GLOBAL RETAIL<br>MORTGAGE BROKER</h1>
  <a class="btn">READ MORE</a>
  <div class="dots"><i></i><i></i><i class="on"></i><i></i><i></i></div>
</header>

<h2 class="sec-title heading" style="top:710px">WHAT WE DO</h2>
<div class="rule" style="left:582px;top:755px;width:36px"></div>

<div class="vline" style="left:421px"></div>
<div class="vline" style="left:777px"></div>

<div class="service" style="left:69px;top:818px">
  <svg width="56" height="62" viewBox="0 0 56 62"><path d="M4 36 L28 14 L52 36" fill="none" stroke="#0c426e" stroke-width="5"/><path d="M10 34 V60 H22 V46 H34 V60 H46 V34" fill="#0c426e"/><circle cx="28" cy="14" r="12" fill="#0c426e"/><text x="28" y="20" text-anchor="middle" fill="#fff" font-size="16" font-family="Poppins" font-weight="700">$</text></svg>
  <h3>Home Purchase Loans</h3>
  <p>Lorem ipsum dolor sit amet conse<br>ctetur adipiscing elit sed do eius mod<br>tempor incididun ullamco.</p>
</div>
<div class="service" style="left:422px;top:818px">
  <svg width="60" height="62" viewBox="0 0 60 62"><g stroke="#0c426e" stroke-width="4" fill="none"><path d="M10 40 V6 M4 12 L10 4 L16 12"/><path d="M30 32 V6 M24 12 L30 4 L36 12"/><path d="M50 40 V6 M44 12 L50 4 L56 12"/></g><circle cx="10" cy="50" r="9" fill="#0c426e"/><circle cx="30" cy="42" r="9" fill="#0c426e"/><circle cx="50" cy="50" r="9" fill="#0c426e"/></svg>
  <h3>Refinance Rates</h3>
  <p>Lorem ipsum dolor sit amet conse<br>ctetur adipiscing elit sed do eius mod<br>tempor incididun ullamco.</p>
</div>
<div class="service" style="left:761px;top:818px">
  <svg width="56" height="58" viewBox="0 0 56 58"><rect x="3" y="3" width="50" height="52" rx="4" fill="none" stroke="#0c426e" stroke-width="4"/><line x1="3" y1="13" x2="53" y2="13" stroke="#0c426e" stroke-width="3"/><circle cx="28" cy="34" r="12" fill="none" stroke="#0c426e" stroke-width="4"/><rect x="23" y="32" width="3" height="7" fill="#0c426e"/><rect x="29" y="29" width="3" height="10" fill="#0c426e"/></svg>
  <h3>Rate Comparisons</h3>
  <p>Lorem ipsum dolor sit amet conse<br>ctetur adipiscing elit sed do eius mod<br>tempor incididun ullamco.</p>
</div>

<div class="service" style="left:69px;top:1052px">
  <svg width="62" height="60" viewBox="0 0 62 60"><circle cx="31" cy="16" r="13" fill="none" stroke="#0c426e" stroke-width="4"/><text x="31" y="22" text-anchor="middle" fill="#0c426e" font-size="16" font-family="Poppins" font-weight="700">$</text><path d="M4 22 L8 50 L20 58 L22 40 L12 30 Z M58 22 L54 50 L42 58 L40 40 L50 30 Z" fill="#0c426e"/></svg>
  <h3>Fast Funding</h3>
  <p>Lorem ipsum dolor sit amet conse<br>ctetur adipiscing elit sed do eius mod<br>tempor incididun ullamco.</p>
</div>
<div class="service" style="left:422px;top:1052px">
  <svg width="50" height="62" viewBox="0 0 50 62"><circle cx="25" cy="12" r="9" fill="none" stroke="#0c426e" stroke-width="4"/><path d="M25 21 V28" stroke="#0c426e" stroke-width="4"/><rect x="8" y="28" width="34" height="32" fill="#0c426e"/><g fill="#fff"><rect x="14" y="34" width="5" height="5"/><rect x="22" y="34" width="5" height="5"/><rect x="30" y="34" width="5" height="5"/><rect x="14" y="43" width="5" height="5"/><rect x="30" y="43" width="5" height="5"/><rect x="21" y="48" width="8" height="12"/></g></svg>
  <h3>Evaluate Your Property</h3>
  <p>Lorem ipsum dolor sit amet conse<br>ctetur adipiscing elit sed do eius mod<br>tempor incididun ullamco.</p>
</div>
<div class="service" style="left:761px;top:1052px">
  <svg width="66" height="58" viewBox="0 0 66 58"><g fill="none" stroke="#0c426e" stroke-width="4" stroke-linejoin="round"><path d="M4 18 L30 6 L62 22 L36 34 Z"/><path d="M4 28 L36 44 L62 32"/><path d="M4 38 L36 54 L62 42"/></g></svg>
  <h3>Cash-Out Refinance</h3>
  <p>Lorem ipsum dolor sit amet conse<br>ctetur adipiscing elit sed do eius mod<br>tempor incididun ullamco.</p>
</div>

<div class="about-photo" role="img" aria-label="Father and young daughter washing hands together at a kitchen sink"></div>
<section class="about-panel">
  <div class="kicker">About Us</div>
  <h2>Calderon Lending</h2>
  <div class="bar"></div>
  <p>Nam libero tempore, cum soluta nobis est eligendi optio cumque nihil impedit quo minus id quod maxime placeat facere possimus, omnis voluptas assumenda est, omnis dolor repellendus. Temporibus autem quibusdam et aut officiis debitis aut rerum necessitatibus saepe eveniet ut et voluptates repudiandae sint et molestiae non recusandae.</p>
  <a class="btn">READ MORE</a>
</section>

<section class="why">
  <h2 class="heading">WHY CHOOSE US</h2>
  <div class="bar"></div>
  <div class="reason active" style="top:145px">
    <div class="ico"><svg width="30" height="28" viewBox="0 0 30 28"><rect x="2" y="3" width="22" height="16" fill="none" stroke="#0c426e" stroke-width="2.5"/><circle cx="19" cy="14" r="6" fill="#fff" stroke="#0c426e" stroke-width="2.5"/><line x1="23" y1="18" x2="28" y2="24" stroke="#0c426e" stroke-width="3"/><line x1="8" y1="24" x2="16" y2="24" stroke="#0c426e" stroke-width="2.5"/></svg></div>
    <h4>Refinance Analysis</h4>
    <p>Nam libero tempore, cum soluta nobis est eligendi optio cumque nihil impedit.</p>
  </div>
  <div class="reason" style="top:245px">
    <div class="ico"><svg width="22" height="28" viewBox="0 0 22 28"><rect x="2" y="2" width="18" height="24" rx="2" fill="none" stroke="#fff" stroke-width="2"/><rect x="5" y="5" width="12" height="6" fill="#fff"/><g fill="#fff"><rect x="5" y="14" width="3" height="3"/><rect x="10" y="14" width="3" height="3"/><rect x="15" y="14" width="2" height="3"/><rect x="5" y="19" width="3" height="3"/><rect x="10" y="19" width="3" height="3"/><rect x="15" y="19" width="2" height="3"/></g></svg></div>
    <h4>Mortgage Rates</h4>
    <p>Nam libero tempore, cum soluta nobis est eligendi optio cumque nihil impedit.</p>
  </div>
  <div class="reason" style="top:345px">
    <div class="ico"><svg width="26" height="26" viewBox="0 0 26 26"><rect x="2" y="11" width="5" height="13" fill="#fff"/><path d="M9 11 L14 2 C17 2 17 5 16 9 H23 C25 9 25 12 23 13 C25 14 24 17 22 17 C24 18 23 21 21 21 C22 23 21 24 19 24 H9 Z" fill="#fff"/></svg></div>
    <h4>Customer Satisfaction</h4>
    <p>Nam libero tempore, cum soluta nobis est eligendi optio cumque nihil impedit.</p>
  </div>
  <div class="reason" style="top:445px">
    <div class="ico"><svg width="28" height="28" viewBox="0 0 28 28"><path d="M5 16 V13 A9 9 0 0 1 23 13 V16" fill="none" stroke="#fff" stroke-width="2.5"/><rect x="3" y="14" width="5" height="9" rx="2" fill="#fff"/><rect x="20" y="14" width="5" height="9" rx="2" fill="#fff"/><path d="M22 23 Q22 26 16 26" fill="none" stroke="#fff" stroke-width="2"/></svg></div>
    <h4>Support</h4>
    <p>Nam libero tempore, cum soluta nobis est eligendi optio cumque nihil impedit.</p>
  </div>
  <div class="why-photo" role="img" aria-label="Modern two-storey home with lit glass walls at dusk in the snow"></div>
</section>

<h2 class="sec-title heading" style="top:2383px">TESTIMONIALS</h2>
<div class="rule" style="left:582px;top:2428px;width:36px"></div>

<svg class="arrow" style="left:84px" width="14" height="24" viewBox="0 0 14 24"><path d="M12 2 L2 12 L12 22" fill="none" stroke="#aaa" stroke-width="2"/></svg>
<svg class="arrow" style="left:1098px" width="14" height="24" viewBox="0 0 14 24"><path d="M2 2 L12 12 L2 22" fill="none" stroke="#aaa" stroke-width="2"/></svg>

<article class="t-card" style="left:133px"><span class="q">“</span><span class="stars">★★★★★</span><p>On the other hand, we denounce with righteous indignation and dislike men who are so beguiled and demoralized by the charms of pleasure of the moment, so blinded by desire, that they cannot foresee the pain</p><span class="bar"></span><span class="who">MARISOL</span></article>
<article class="t-card" style="left:370px"><span class="q">“</span><span class="stars">★★★★★</span><p>On the other hand, we denounce with righteous indignation and dislike men who are so beguiled and demoralized by the charms of pleasure of the moment, so blinded by desire, that they cannot foresee the pain</p><span class="bar"></span><span class="who">MARISOL</span></article>
<article class="t-card" style="left:607px"><span class="q">“</span><span class="stars">★★★★★</span><p>On the other hand, we denounce with righteous indignation and dislike men who are so beguiled and demoralized by the charms of pleasure of the moment, so blinded by desire, that they cannot foresee the pain</p><span class="bar"></span><span class="who">MARISOL</span></article>
<article class="t-card" style="left:843px"><span class="q">“</span><span class="stars">★★★★★</span><p>On the other hand, we denounce with righteous indignation and dislike men who are so beguiled and demoralized by the charms of pleasure of the moment, so blinded by desire, that they cannot foresee the pain</p><span class="bar"></span><span class="who">MARISOL</span></article>

<section class="quote" role="img" aria-label="Faded aerial view of a residential neighbourhood behind the rate quote call to action">
  <h2 class="heading">Get a Rate Quote in Just 30 Seconds!</h2>
  <p>On the other hand, we denounce with righteous indignation and dislike men who are so beguiled and demoralized by the charms of pleasure of the moment.</p>
  <a class="btn">GET MY CUSTOM RATE QUOTE RATE NOW!</a>
</section>

<footer class="footer">
  <div class="f-brand">
    <div class="mark"></div>
    <div class="name">CALDERON LENDING</div>
    <div class="tag">a retail mortgage broker</div>
  </div>
  <div class="f-col">
    <h5 style="left:458px;top:61px">MENU</h5>
    <ul class="f-menu">
      <li>HOME</li><li>ABOUT US</li><li>SERVICES</li><li>MORTGAGES</li><li>REFINANCING</li><li>BLOG</li><li>CONTACT US</li>
    </ul>
  </div>
  <div class="f-col">
    <h5 style="left:654px;top:61px">CONTACT US</h5>
    <div class="f-item" style="left:652px;top:103px"><span class="dot"><svg width="12" height="14" viewBox="0 0 12 14"><path d="M6 14 C2 9 1 7 1 5 A5 5 0 0 1 11 5 C11 7 10 9 6 14Z" fill="#2b2b2b"/><circle cx="6" cy="5" r="2" fill="#fff"/></svg></span><span>4471 Harbor Crest Lane<br>Bowie, MD 20715</span></div>
    <div class="f-item" style="left:652px;top:165px"><span class="dot"><svg width="12" height="12" viewBox="0 0 12 12"><path d="M2 1 L4.5 1 L5.5 4 L4 5 C5 7 6 8 7 8 L8 6.5 L11 7.5 L11 10 C11 11 10 11 9 11 C5 11 1 7 1 3 C1 2 1 1 2 1Z" fill="#2b2b2b"/></svg></span><span>Call Us<br>555.014.2290</span></div>
    <div class="f-item" style="left:652px;top:226px"><span class="dot"><svg width="12" height="10" viewBox="0 0 12 10"><rect x="0.5" y="0.5" width="11" height="9" fill="#2b2b2b"/><path d="M1 1 L6 5.5 L11 1" fill="none" stroke="#fff" stroke-width="1"/></svg></span><span>E mail Us<br>hello@calderonlending.com</span></div>
  </div>
  <div class="f-col">
    <h5 style="left:940px;top:61px">FOLLOW US</h5>
    <div class="f-item" style="left:940px;top:103px"><span class="dot"></span><span>Like us on<br>NEIGHBORLY</span></div>
    <div class="f-item" style="left:940px;top:165px"><span class="dot"></span><span>Follow us on<br>CHIRPLINE</span></div>
    <div class="f-item" style="left:940px;top:226px"><span class="dot"></span><span>Follow us on<br>WORKRANK</span></div>
  </div>
  <div class="f-rule"></div>
  <div class="copy">Copyright © 2020 All Rights Reserved</div>
</footer>

</body>
</html>
```